Visitenkarten-Design für Vermittlung und Verkauf von Immobilien
Perfekte Umsetzung meiner Wünsche, sowie auch selbständige Einbringung von Ideen. Sehr zu empfehlen!
Zielgruppe
Immobilien vermitteln, verkaufen

```html
<!DOCTYPE html>
<html lang="de">
<head>
<meta charset="utf-8">
<title>Halvaro Immobilien – Visitenkarte</title>
<link rel="stylesheet" href="https://fonts.googleapis.com/css2?family=Open+Sans:wght@400;600&display=swap">
<style>
  :root {
    --stage: #000000;
    --paper: #ffffff;
    --navy: #16294a;
    --sky: #c5dff5;
    --ink: #1b1b1b;
    --muted: #5b5b5b;
    --accent: #1f9ad6;
  }
  * { margin: 0; padding: 0; box-sizing: border-box; }
  html, body { width: 1200px; height: 1200px; overflow: hidden; background: var(--stage); }
  body { position: relative; font-family: "Open Sans", Arial, sans-serif; }

  .card { position: absolute; overflow: hidden; }
  .card--front { left: 296px; top: 84px; width: 620px; height: 402px; background: var(--paper); }
  .card--back  { left: 283px; top: 564px; width: 610px; height: 393px; background: var(--sky); }

  .brand-name {
    position: absolute;
    text-align: center;
    color: var(--navy);
    font-weight: 600;
    font-size: 34px;
    line-height: 1.15;
    letter-spacing: 0.16em;
    text-transform: uppercase;
  }
  .card--front .brand-name { left: 20px; width: 300px; top: 200px; }
  .card--back .brand-name { left: 0; width: 610px; top: 238px; }

  .holder { position: absolute; left: 387px; top: 86px; }
  .holder__name { font-size: 24px; color: var(--ink); font-weight: 400; line-height: 1.25; }
  .holder__role { font-size: 18px; color: var(--muted); line-height: 1.3; }

  .contact { position: absolute; left: 392px; top: 204px; list-style: none; font-size: 15.5px; color: var(--muted); }
  .contact li { display: flex; align-items: flex-start; gap: 8px; line-height: 23px; margin-bottom: 4px; }
  .contact svg { flex: none; width: 18px; height: 18px; margin-top: 3px; }
  .contact li.address { margin-bottom: 12px; }

  .footer-band { position: absolute; left: 0; bottom: 0; width: 620px; height: 41px; }
  .web { position: absolute; left: 400px; bottom: 0; height: 41px; display: flex; align-items: center; gap: 10px; color: var(--paper); font-size: 17px; }
  .web svg { width: 17px; height: 17px; }
</style>
</head>
<body>

<section class="card card--front" aria-label="Visitenkarte Vorderseite">
  <div class="brand-name">Halvaro<br>Immobilien</div>

  <div class="holder">
    <p class="holder__name">Lena Halvaro</p>
    <p class="holder__role">Geschäftsführend</p>
  </div>

  <ul class="contact">
    <li class="address">
      <svg viewBox="0 0 18 18"><path d="M9 1a5.5 5.5 0 0 0-5.5 5.5C3.5 10.5 9 17 9 17s5.5-6.5 5.5-10.5A5.5 5.5 0 0 0 9 1zm0 7.5a2 2 0 1 1 0-4 2 2 0 0 1 0 4z" fill="var(--accent)"/></svg>
      <span>Am Lindenhang 12<br>55131 Mainz</span>
    </li>
    <li>
      <svg viewBox="0 0 18 18"><path d="M4 1.5l3 3-1.6 2a10 10 0 0 0 6.1 6.1l2-1.6 3 3-2 2C8 16 2 10 2 3.5z" fill="none" stroke="var(--muted)" stroke-width="1.5"/></svg>
      <span>00000/ 4418826</span>
    </li>
    <li>
      <svg viewBox="0 0 18 18"><rect x="5" y="2" width="8" height="4" fill="none" stroke="var(--muted)" stroke-width="1.4"/><rect x="2" y="6" width="14" height="7" rx="1" fill="var(--muted)"/><rect x="5" y="11" width="8" height="5" fill="#fff" stroke="var(--muted)" stroke-width="1.4"/></svg>
      <span>00000/ 4418827</span>
    </li>
    <li>
      <svg viewBox="0 0 18 18"><rect x="1.5" y="4" width="15" height="11" fill="none" stroke="var(--muted)" stroke-width="1.5"/><path d="M1.5 4L9 10l7.5-6" fill="none" stroke="var(--muted)" stroke-width="1.5"/></svg>
      <span>Info@halvaro.online</span>
    </li>
  </ul>

  <svg class="footer-band" viewBox="0 0 620 41" aria-hidden="true">
    <rect x="0" y="0" width="265" height="41" fill="var(--sky)"/>
    <polygon points="278,41 293,0 303,0 288,41" fill="var(--sky)"/>
    <polygon points="300,41 315,0 325,0 310,41" fill="var(--sky)"/>
    <polygon points="322,41 337,0 347,0 332,41" fill="var(--sky)"/>
    <polygon points="350,41 365,0 620,0 620,41" fill="var(--navy)"/>
  </svg>
  <div class="web">
    <svg viewBox="0 0 18 18"><circle cx="9" cy="9" r="7.5" fill="none" stroke="#fff" stroke-width="1.4"/><ellipse cx="9" cy="9" rx="3.2" ry="7.5" fill="none" stroke="#fff" stroke-width="1.2"/><path d="M1.5 9h15M3 5h12M3 13h12" stroke="#fff" stroke-width="1.1"/></svg>
    <span>www.halvaro.online</span>
  </div>
</section>

<section class="card card--back" aria-label="Visitenkarte Rückseite">
  <div class="brand-name">Halvaro<br>Immobilien</div>
</section>

</body>
</html>
```